Velmora - 3D medical animations and high end visual content

Our company creates high end visual content and animations for medical global companies.
Our website - www.velmora-studio.example
We would like to have an amazing business card for our CEO that he can use in the following exhebitions he is going to attend.
It is very important that the design will be memorable and diffrent. It has to reflect our brand design (you can have it from our website)
We would like to transmit innovation, prestige, luxury, aesthetics.
The card has to be Double Sided

Target Market(s)

Marketing managers in medical global companys

Industry/Entity Type

It Company

Contact Information for Business Card

Requirements
Nice to have
• It is very important that the design will be memorable and diffrent. It has to reflect our brand design (you can have it from our website)

```html
<!DOCTYPE html>
<html lang="en">
<head>
<meta charset="utf-8">
<title>Velmora – Business Card</title>
<link rel="stylesheet" href="https://fonts.googleapis.com/css2?family=Source+Sans+3:wght@400;600;700&display=swap">
<style>
  :root {
    --page-bg: #e9e6e2;
    --card-top: #0f2c38;
    --card-mid: #0c1a22;
    --card-bottom: #0a0d10;
    --accent-teal: #1d8c9a;
    --text-light: #e4e6e8;
    --accent-gold: #c8963e;
    --brand-tone: #d9d2cc;
  }
  * { margin: 0; padding: 0; box-sizing: border-box; }
  html, body {
    width: 1200px;
    height: 1010px;
    overflow: hidden;
    background: var(--page-bg);
    font-family: "Source Sans 3", "Segoe UI", sans-serif;
  }
  .card {
    position: absolute;
    left: 100px;
    top: 216px;
    width: 1000px;
    height: 578px;
    border-radius: 4px;
    overflow: hidden;
    background:
      radial-gradient(ellipse 70% 80% at 10% 0%, var(--card-top) 0%, transparent 70%),
      linear-gradient(160deg, var(--card-mid) 0%, var(--card-bottom) 100%);
    box-shadow: 0 16px 40px rgba(0,0,0,0.25);
  }
  .holder { position: absolute; left: 45px; top: 72px; }
  .holder-name {
    font-size: 38px;
    font-weight: 700;
    color: var(--accent-teal);
    letter-spacing: 0.2px;
    line-height: 1.1;
  }
  .holder-role {
    margin-top: 4px;
    font-size: 21px;
    font-weight: 400;
    color: var(--text-light);
  }
  .contacts {
    position: absolute;
    left: 50px;
    top: 394px;
    list-style: none;
  }
  .contact-item {
    display: flex;
    align-items: center;
    height: 33px;
    font-size: 23px;
    white-space: nowrap;
    color: var(--text-light);
  }
  .contact-icon { width: 22px; height: 22px; margin-right: 22px; flex: none; }
  .contact-icon * { fill: none; stroke: var(--accent-teal); stroke-width: 1.8; }
  .contact-icon .solid { fill: var(--accent-teal); stroke: none; }
  .contact-icon .fold { stroke: var(--card-bottom); }
  .web-brand { color: var(--accent-gold); }
  .brand-name {
    position: absolute;
    left: 526px;
    top: 432px;
    width: 420px;
    text-align: center;
    font-size: 58px;
    font-weight: 600;
    letter-spacing: 6px;
    color: var(--brand-tone);
    line-height: 1;
  }
</style>
</head>
<body>
  <section class="card" aria-label="Business card front">
    <header class="holder">
      <h1 class="holder-name">Eitan Rosel</h1>
      <p class="holder-role">Founder &amp; CEO</p>
    </header>

    <ul class="contacts">
      <li class="contact-item">
        <svg class="contact-icon" viewBox="0 0 22 22" aria-hidden="true">
          <rect x="6" y="2" width="10" height="18" rx="1.5"/>
          <circle class="solid" cx="11" cy="17" r="1"/>
        </svg>
        +000-55-0142376
      </li>
      <li class="contact-item">
        <svg class="contact-icon" viewBox="0 0 22 22" aria-hidden="true">
          <path class="solid" d="M2 8c0-3 4-5 9-5s9 2 9 5v2h-5V8H7v2H2z"/>
          <path class="solid" d="M5 12h12l2 7H3z"/>
        </svg>
        +000-55-0198420
      </li>
      <li class="contact-item">
        <svg class="contact-icon" viewBox="0 0 22 22" aria-hidden="true">
          <rect class="solid" x="2" y="5" width="18" height="12"/>
          <path class="fold" d="M2 5l9 7 9-7"/>
        </svg>
        eitan@velmora-studio.example
      </li>
      <li class="contact-item">
        <svg class="contact-icon" viewBox="0 0 22 22" aria-hidden="true">
          <circle cx="11" cy="11" r="8.5"/>
          <ellipse cx="11" cy="11" rx="3.8" ry="8.5"/>
          <line x1="2.5" y1="11" x2="19.5" y2="11"/>
        </svg>
        <span>www.<span class="web-brand">velmora</span>-studio.example</span>
      </li>
    </ul>

    <p class="brand-name">VELMORA</p>
  </section>
</body>
</html>
```